Label Design for honey from a small farm in Italy

We need a label for our Acacia's honey .
We are a little farm in Italy and we would like something like organic, raw and simple.
Maybe with botanical drawing with different color like watercolor o something like that (very important natural and easy)
the jar for 1kg of honey: Capacity: 780 ml - Height: 137 mm - Diameter: ∅ 94 mm
- size approx h 5,5 x 10/14cm ( we use the same label for kg and 500 gr jar)

Industry/Entity Type

Farm

Requirements
Must have
• the writings:
- Acacia
- Miele italiano di Acacia
- Da consumarsi preferibilmente entro: ( and below the space to put the date by the hands)
- some space to put some presentation of the farm or some phrases
- our logo
- the space to put the weight by the hands
- Prodotto da Azienda Agricola ...(produced by Farm Name and address....)
- Confezionato presso Apicoltura... (packaged at apiculture Name and address..)
- graphic of Acacia’s flowers ( like drawing)
Should not have
• Barcode
nutritional table

```html
<!DOCTYPE html>
<html lang="it">
<head>
<meta charset="utf-8">
<title>Miele di Acacia – etichetta</title>
<link href="https://fonts.googleapis.com/css2?family=Bebas+Neue&family=Montserrat:wght@400;500;600;700&display=swap" rel="stylesheet">
<style>
  :root {
    --mint: #a3d8c6;
    --mint-line: #9fd3c1;
    --ink: #1f1f1f;
    --paper: #ffffff;
    --page: #f2f2f0;
    --flower-a: #f6dd3a;
    --flower-b: #8fb98a;
  }
  * { box-sizing: border-box; margin: 0; padding: 0; }
  html, body { width: 889px; height: 1200px; overflow: hidden; }
  body {
    background: var(--page);
    font-family: "Montserrat", sans-serif;
    color: var(--ink);
    position: relative;
  }
  .label {
    position: absolute;
    left: 24px; top: 420px;
    width: 840px; height: 360px;
    background: var(--paper);
    overflow: hidden;
    box-shadow: 0 6px 24px rgba(0,0,0,.18);
  }
  .label__shapes { position: absolute; inset: 0; width: 100%; height: 100%; }
  .copy {
    position: absolute;
    width: 220px;
    font-size: 9.2px;
    line-height: 12px;
    text-align: justify;
    text-align-last: left;
  }
  .info-box {
    position: absolute;
    width: 220px; height: 28px;
    border: 1.5px solid var(--mint-line);
    background: var(--paper);
    display: flex; align-items: center; justify-content: center;
    font-size: 11px; letter-spacing: .1px;
    white-space: nowrap;
  }
  .col-left .copy, .col-left .info-box { left: 27px; }
  .col-right .copy, .col-right .info-box { left: 609px; }
  .copy--top { top: 38px; }
  .copy--bottom { top: 187px; }
  .info-box--producer { top: 147px; }
  .info-box--packer { top: 293px; }
  .info-box--packer, .col-left .info-box--producer { background: var(--paper); }

  .brand {
    position: absolute; left: 340px; top: 28px; width: 160px;
    display: flex; align-items: center; justify-content: center; gap: 6px;
    color: var(--mint); font-weight: 700; font-size: 15px; letter-spacing: .5px;
  }
  .brand__dot { width: 10px; height: 10px; border-radius: 50%; background: var(--mint); }
  .product-name {
    position: absolute; left: 320px; top: 74px; width: 200px;
    text-align: center;
    font-family: "Bebas Neue", sans-serif;
    font-size: 76px; line-height: 66px;
    color: var(--mint); letter-spacing: 1px;
  }
  .product-rule {
    position: absolute; left: 336px; top: 141px; width: 167px; height: 2px;
    background: var(--mint);
  }
  .product-sub {
    position: absolute; left: 310px; top: 151px; width: 220px;
    text-align: center; font-weight: 600; font-size: 11.5px; letter-spacing: .2px;
  }
  .flower-art {
    position: absolute; left: 338px; top: 180px; width: 200px; height: 180px;
    background: radial-gradient(ellipse at 45% 45%, var(--flower-a) 0%, #f1d94a 45%, rgba(143,185,138,.7) 80%, rgba(143,185,138,0) 100%);
    border-radius: 45% 55% 0 0;
  }
  .net-weight {
    position: absolute; left: 378px; top: 333px; width: 84px; height: 15px;
    border-radius: 8px;
    background: rgba(255,255,255,.35);
    color: #fff; font-size: 7px;
    display: flex; align-items: center; justify-content: center; gap: 6px;
  }
  .best-before {
    position: absolute; left: 658px; top: 304px;
    font-size: 8.8px; line-height: 12px; font-weight: 700;
  }
</style>
</head>
<body>
  <main class="label">
    <svg class="label__shapes" viewBox="0 0 1538 660" preserveAspectRatio="none" aria-hidden="true">
      <path fill="var(--mint)" d="M0 0 H330 C430 40 410 140 330 200 C250 260 200 330 260 400 C300 460 210 520 110 500 C60 490 30 460 0 440 Z"/>
      <path fill="var(--mint)" d="M1538 225 C1440 195 1320 230 1300 330 C1285 400 1300 440 1220 485 C1150 530 1140 620 1200 660 H1538 Z"/>
      <path fill="var(--mint)" d="M560 520 C525 420 585 360 645 345 C725 320 765 430 865 430 C985 430 1065 520 1043 600 C1033 640 1013 660 993 660 H620 C585 630 570 580 560 520 Z"/>
    </svg>

    <section class="col-left">
      <p class="copy copy--top">Lorem ipsum dolor sit amet, consectetuer adipiscing elit, sed diam nonummy nibh euismod tincidunt ut laoreet dolore magna aliquam erat volutpat. Ut wisi enim ad minim veniam, quis nostrud exerci tation ullamcorper suscipit lobortis nisl ut aliquip ex ea commodo consequat. Duis autem vel eum iriure dolor in hendrerit in vulputate vadipiscing elit, sed diam nonummy nibh</p>
      <div class="info-box info-box--producer">PRODOTTO DA AZIENDA AGRICOLA</div>
      <p class="copy copy--bottom">Lorem ipsum dolor sit amet, consectetuer adipiscing elit, sed diam nonummy nibh euismod tincidunt ut laoreet dolore magna aliquam erat volutpat. Ut wisi enim ad minim veniam, quis nostrud exerci tation ullamcorper suscipit lobortis nisl ut aliquip ex ea commodo consequat. Duis autem vel eum iriure dolor in hendrerit in vulputate vadipiscing elit, sed diam nonummy nibh</p>
      <div class="info-box info-box--packer">CONFEZIONATO PRESSO APICOLTURA</div>
    </section>

    <section class="col-center">
      <div class="brand"><span class="brand__dot"></span><span>IL PODERINO</span></div>
      <h1 class="product-name">ACACIA</h1>
      <div class="product-rule"></div>
      <p class="product-sub">MIELE ITALIANO DI ACACIA</p>
      <div class="flower-art" role="img" aria-label="Illustrazione ad acquerello di un ramo di acacia con fiori gialli e foglie verdi"></div>
      <div class="net-weight"><span>Nt Weight</span><span>00.00</span></div>
    </section>

    <section class="col-right">
      <p class="copy copy--top">Lorem ipsum dolor sit amet, consectetuer adipiscing elit, sed diam nonummy nibh euismod tincidunt ut laoreet dolore magna aliquam erat volutpat. Ut wisi enim ad minim veniam, quis nostrud exerci tation ullamcorper suscipit lobortis nisl ut aliquip ex ea commodo consequat. Duis autem vel eum iriure dolor in hendrerit in vulputate vadipiscing elit, sed diam nonummy nibh</p>
      <div class="info-box info-box--producer">PRODOTTO DA AZIENDA AGRICOLA</div>
      <p class="copy copy--bottom">Lorem ipsum dolor sit amet, consectetuer adipiscing elit, sed diam nonummy nibh euismod tincidunt ut laoreet dolore magna aliquam erat volutpat. Ut wisi enim ad minim veniam, quis nostrud exerci tation ullamcorper suscipit lobortis nisl ut aliquip ex ea commodo consequat. Duis autem vel eum iriure dolor in hendrerit in vulputate vadipiscing elit, sed diam nonummy nibh</p>
      <p class="best-before">Da consumarsi<br>preferibilmente entro:</p>
    </section>
  </main>
</body>
</html>
```